A postcard needed for a kids gym

We are a kids gym opening soon. We are called Brightleap Kids Gym. Here is the website so that you can get more details on what it is we will be doing. www.Brightleapkidsgym.example I am including a screen shot of wallpaper we are using on two walls that will be prominently displayed in our building. I was wondering if the wall paper can somehow be included in the postcard as a soft background or something?no postage or mail info needed as this will be passed out by hand. I am also sending our logo and colors. Thank you for your help, and we look forward to hearing and seeing what you have to present. Sincerely,Rosalind

Target Market(s)

Parents

Industry/Entity Type

Childcare

Requirements
Must have
• "Opening soon"

```html
<!DOCTYPE html>
<html lang="en">
<head>
<meta charset="utf-8">
<title>Brightleap Kids Gym – Opening Soon Postcard</title>
<link rel="stylesheet" href="https://fonts.googleapis.com/css2?family=Luckiest+Guy&family=Raleway:wght@400;500;700&display=swap">
<style>
  :root {
    --teal: #6dc3bf;
    --orange: #f7a93b;
    --green: #8cc63f;
    --blue: #29abe2;
    --yellow: #fcd116;
    --white: #ffffff;
    --ink: #4a4a4a;
    --page: #eeeeee;
    --photo-cool: #3f7fc4;
  }
  * { box-sizing: border-box; margin: 0; padding: 0; }
  html, body { width: 895px; height: 1200px; overflow: hidden; }
  body { background: var(--page); font-family: "Raleway", sans-serif; position: relative; }

  .postcard {
    position: absolute; width: 696px; height: 537px;
    background: var(--white); overflow: hidden;
    box-shadow: 0 4px 14px rgba(0,0,0,.18);
  }
  .postcard--front { left: 62px; top: 44px; }
  .postcard--back { left: 140px; top: 615px; }

  .shape-layer { position: absolute; inset: 0; width: 100%; height: 100%; }

  .photo { position: absolute; }
  .photo--blocks { left: 342px; top: 249px; width: 354px; height: 288px;
    background: linear-gradient(135deg, var(--yellow) 0%, #e8403a 40%, var(--photo-cool) 75%, var(--green) 100%); }
  .photo--playground { left: 280px; top: 0; width: 416px; height: 180px;
    background: linear-gradient(90deg, #b9a58d 0%, #d8c7ae 45%, #5f7c4a 100%); }
  .photo--map { left: 0; top: 249px; width: 311px; height: 149px; background: #ebe8e2; }
  .photo--party { left: 0; top: 398px; width: 187px; height: 139px;
    background: linear-gradient(135deg, #f29bc1 0%, #f6c644 55%, #6cb4e4 100%); }
  .photo--crafts { left: 189px; top: 398px; width: 122px; height: 139px;
    background: linear-gradient(135deg, #fbe3c5 0%, #f0a35c 60%, #7fc3e6 100%); }

  .intro { position: absolute; color: var(--white); }
  .intro--front { left: 32px; top: 26px; }
  .intro__title { font-weight: 400; font-size: 27px; line-height: 1.15; }
  .intro__sub { font-size: 15px; line-height: 1.35; margin-top: 14px; }
  .intro--back { left: 36px; top: 36px; font-size: 18px; line-height: 1.25; }
  .intro--back .intro__name { margin-bottom: 14px; }

  .brand-name {
    position: absolute; font-family: "Raleway", sans-serif; font-weight: 700;
    color: var(--blue); text-align: center; line-height: 1.05;
  }
  .brand-name--front { left: 298px; top: 38px; width: 360px; font-size: 44px; }
  .brand-name--back { left: 413px; top: 268px; width: 236px; font-size: 30px; }

  .headline {
    position: absolute; left: 0; top: 188px; width: 100%; text-align: center;
    font-family: "Luckiest Guy", sans-serif; color: var(--white);
    text-transform: uppercase; letter-spacing: 2px; font-size: 52px; line-height: 1;
  }

  .about {
    position: absolute; left: 0; top: 249px; width: 342px; height: 238px;
    background: var(--green); color: var(--white); padding: 18px 58px 0 28px;
  }
  .about__name { font-size: 19px; font-weight: 500; margin-bottom: 8px; }
  .about__text { font-size: 15px; line-height: 23px; text-align: justify; }

  .website-bar {
    position: absolute; background: var(--white); color: var(--ink);
    font-size: 17px; display: flex; align-items: center; padding-left: 32px;
  }
  .postcard--front .website-bar { left: 0; top: 487px; width: 338px; height: 36px; }
  .postcard--front .website-strip { position: absolute; left: 0; top: 523px; width: 342px; height: 14px; background: var(--green); }
  .postcard--back .website-bar { left: 354px; top: 484px; width: 342px; height: 38px;
    background: var(--green); color: var(--white); padding-left: 34px; }

  .services { position: absolute; list-style: none; }
  .services__item {
    position: absolute; width: 76px; height: 76px; border-radius: 50%;
    display: flex; align-items: center; justify-content: center;
    color: var(--white); font-size: 16px;
    box-shadow: 0 2px 4px rgba(0,0,0,.15);
  }
  .services__item--play { background: var(--blue); }
  .services__item--parties { background: var(--orange); }
  .services__item--classes { background: var(--yellow); }

  .details {
    position: absolute; left: 404px; top: 358px; width: 262px;
    font-size: 13.5px; line-height: 1.2; color: var(--ink); text-align: justify;
  }
</style>
</head>
<body>

<section class="postcard postcard--front" aria-label="Postcard front">
  <div class="photo photo--blocks" role="img" aria-label="Photo of smiling children playing among large colourful foam blocks"></div>

  <svg class="shape-layer" viewBox="0 0 696 537" aria-hidden="true">
    <path d="M0 0 H270 C300 40 305 140 285 186 H0 Z" fill="var(--teal)"/>
    <path d="M0 186 C200 160 480 160 696 168 V249 H0 Z" fill="var(--orange)"/>
  </svg>

  <div class="intro intro--front">
    <p class="intro__title">OPENING<br>December 2015</p>
    <p class="intro__sub">Indoor play space &amp;<br>treatment center</p>
  </div>

  <p class="brand-name brand-name--front">Brightleap<br>Kids Gym</p>

  <h1 class="headline">Opening Soon</h1>

  <div class="about">
    <p class="about__name">Brightleap Kids Gym</p>
    <p class="about__text">provides fun for the entire family with an inclusive indoor play area, designated space for parties or celebrations, and a variety of motivating, kid-centered classes. We also offer private therapy services you can easily schedule by phone or online.</p>
  </div>

  <p class="website-bar">www.Brightleapkidsgym.example</p>
  <div class="website-strip"></div>

  <ul class="services">
    <li class="services__item services__item--play" style="left:298px;top:255px">play</li>
    <li class="services__item services__item--parties" style="left:298px;top:330px">parties</li>
    <li class="services__item services__item--classes" style="left:298px;top:406px">classes</li>
  </ul>
</section>

<section class="postcard postcard--back" aria-label="Postcard back">
  <div class="photo photo--playground" role="img" aria-label="Photo of the indoor wooden play structure with rope bridge and forest wallpaper"></div>
  <div class="photo photo--map" role="img" aria-label="Street map showing the gym location"></div>
  <div class="photo photo--party" role="img" aria-label="Photo of a children's birthday party with balloons"></div>
  <div class="photo photo--crafts" role="img" aria-label="Photo of children playing with colourful toys"></div>

  <svg class="shape-layer" viewBox="0 0 696 537" aria-hidden="true">
    <path d="M0 0 H285 C312 50 312 140 292 178 H0 Z" fill="var(--teal)"/>
    <path d="M0 180 C200 160 480 160 696 168 V249 H0 Z" fill="var(--orange)"/>
  </svg>

  <div class="intro intro--back">
    <p class="intro__name">Brightleap Kids Gym</p>
    <p>2480 Maple Grove Road<br>Fairview, CA 90000<br>brightleapkidsgym.example</p>
  </div>

  <h2 class="headline">Opening Soon</h2>

  <p class="brand-name brand-name--back">Brightleap<br>Kids Gym</p>

  <p class="details">Brightleap Kids Gym (BKGym) is more than an activity center. Our facility offers a safe, inclusive space for kids to play, learn, and explore using all their senses.<br>One-on-one private therapy services are also available by appointment.</p>

  <p class="website-bar">www.Brightleapkidsgym.example</p>

  <ul class="services">
    <li class="services__item services__item--play" style="left:310px;top:254px">play</li>
    <li class="services__item services__item--parties" style="left:310px;top:329px">parties</li>
    <li class="services__item services__item--classes" style="left:310px;top:403px">classes</li>
  </ul>
</section>

</body>
</html>
```